Business Card and Letterhead for Pemlo - modern real estate business

I need a double sided business card design for Pemlo. Please see business card brief here https://files.quillnote-hub.net/page/7RtxQmZbn4LsWe2VyHoPk9dFjuC3gaXrTmqEi5Ns_pz/view?mode=shared

Please feel free to design the business cards however you feel best. I am happy to give some creative freedoms and then provide feedback from there.

Please then also create a letterhead to match the business card design

Colors

Designer to choose colors to be used in the design.

Requirements
Must have
• Must be a modern, elegant business card which looks very professional

```html
<!DOCTYPE html>
<html lang="en">
<head>
<meta charset="utf-8">
<title>Pemlo Business Card</title>
<link href="https://fonts.googleapis.com/css2?family=Roboto+Condensed:wght@300;400;700&display=swap" rel="stylesheet">
<style>
  :root {
    --page-bg: #dcdce2;
    --card-dark: #231f20;
    --brand-red: #e31e26;
    --red-deep: #c41f2e;
    --red-light: #ec4038;
    --band-white: #f2f2f4;
    --pattern-grey: #e4e4e7;
    --ink: #231f20;
    --photo-dark: #2b2a2d;
    --photo-mid: #6b5f5a;
  }
  * { margin: 0; padding: 0; box-sizing: border-box; }
  html, body {
    width: 1200px; height: 1200px; overflow: hidden;
    background: var(--page-bg);
    font-family: "Roboto Condensed", "Arial Narrow", sans-serif;
  }
  .card {
    position: absolute; left: 258px; width: 685px; height: 423px; overflow: hidden;
  }
  .card-front { top: 123px; background: var(--card-dark); display: flex; align-items: center; justify-content: center; }
  .brand-name {
    color: var(--brand-red); font-weight: 700; font-size: 76px; letter-spacing: 10px; line-height: 1;
    padding-left: 10px;
  }
  .card-back { top: 641px; background: var(--band-white); }
  .card-back svg.backdrop { position: absolute; inset: 0; }
  .agent-name {
    position: absolute; left: 35px; top: 30px; color: #fff; font-weight: 700; font-size: 37px; line-height: 1;
  }
  .agent-title {
    position: absolute; left: 35px; top: 78px; color: #fff; font-weight: 300; font-size: 25px; line-height: 1;
  }
  .contact-list { position: absolute; left: 458px; top: 236px; list-style: none; }
  .contact-item {
    display: flex; align-items: flex-start; gap: 8px;
    color: var(--ink); font-weight: 700; font-size: 18px; letter-spacing: 1.2px; line-height: 25px;
    margin-bottom: 13px;
  }
  .contact-item svg { width: 17px; height: 17px; margin-top: 4px; flex: none; }
  .contact-item.web { color: var(--brand-red); }
</style>
</head>
<body>
  <section class="card card-front">
    <div class="brand-name">PEMLO</div>
  </section>

  <section class="card card-back">
    <svg class="backdrop" viewBox="0 0 685 423" width="685" height="423">
      <defs>
        <linearGradient id="redSweep" x1="0" y1="0" x2="1" y2="0">
          <stop offset="0" stop-color="var(--red-light)"/>
          <stop offset="0.2" stop-color="var(--red-deep)"/>
          <stop offset="0.55" stop-color="var(--red-light)"/>
          <stop offset="1" stop-color="var(--red-deep)"/>
        </linearGradient>
        <linearGradient id="photoTone" x1="0" y1="0" x2="0" y2="1">
          <stop offset="0" stop-color="var(--photo-mid)"/>
          <stop offset="0.35" stop-color="var(--photo-dark)"/>
          <stop offset="1" stop-color="var(--photo-dark)"/>
        </linearGradient>
      </defs>
      <polygon class="pattern-field" points="685,64 685,423 0,423 0,405" fill="var(--pattern-grey)"/>
      <polygon class="red-panel" points="0,0 634,0 0,313" fill="url(#redSweep)"/>
      <polygon class="edge-stripe" points="634,0 640,0 0,318 0,313" fill="var(--brand-red)"/>
      <polygon class="lower-stripe" points="685,61 685,68 0,409 0,402" fill="var(--brand-red)"/>
      <rect class="agent-photo" role="img" aria-label="Portrait photo of the agent in a dark suit" x="58" y="127" width="278" height="296" rx="6" fill="url(#photoTone)"/>
    </svg>

    <h1 class="agent-name">Liam Carter</h1>
    <p class="agent-title">Licenced Real Estate Agent</p>

    <ul class="contact-list">
      <li class="contact-item">
        <svg viewBox="0 0 24 24"><path d="M6.6 10.8a15 15 0 0 0 6.6 6.6l2.2-2.2c.3-.3.7-.4 1-.2 1.1.4 2.3.6 3.6.6.6 0 1 .4 1 1V20c0 .6-.4 1-1 1A17 17 0 0 1 3 4c0-.6.4-1 1-1h3.5c.6 0 1 .4 1 1 0 1.3.2 2.5.6 3.6.1.3 0 .7-.2 1z" fill="none" stroke="var(--brand-red)" stroke-width="2"/></svg>
        <span>0400 318 592</span>
      </li>
      <li class="contact-item">
        <svg viewBox="0 0 24 24"><rect x="2" y="5" width="20" height="14" fill="none" stroke="var(--brand-red)" stroke-width="2"/><path d="M2 5l10 8 10-8M2 19l7-7M22 19l-7-7" fill="none" stroke="var(--brand-red)" stroke-width="2"/></svg>
        <span>liam@pemlo.com</span>
      </li>
      <li class="contact-item">
        <svg viewBox="0 0 24 24"><path d="M12 2a7 7 0 0 0-7 7c0 5 7 13 7 13s7-8 7-13a7 7 0 0 0-7-7zm0 9.5A2.5 2.5 0 1 1 12 6.5a2.5 2.5 0 0 1 0 5z" fill="var(--brand-red)"/></svg>
        <span>PO Box 1180<br>Ferndale NSW 2790</span>
      </li>
      <li class="contact-item web">
        <svg viewBox="0 0 24 24"><path d="M10 14a4 4 0 0 0 5.7 0l3.5-3.5a4 4 0 0 0-5.7-5.7l-1.5 1.5M14 10a4 4 0 0 0-5.7 0l-3.5 3.5a4 4 0 0 0 5.7 5.7l1.5-1.5" fill="none" stroke="var(--brand-red)" stroke-width="2" stroke-linecap="round"/></svg>
        <span>www.pemlo.com</span>
      </li>
    </ul>
  </section>
</body>
</html>
```